Flyer-Design für Vermittlung von Betreuungskräften
Zielgruppe
Wir vermitteln Betreuungskräfte aus Osteuropa für pflegebedürftige Menschen in Deutschland. Dabei legen wir Wert auf Seriösität, Professionalität und fürsorgliche Beratung. Folglich sind unsere Zielgruppe ältere Menschen und vor allem deren Angehörige, die für ihre Herzensmenschen entscheiden, ob die Pflege daheim ermöglicht wird. Der Flyer soll Wärme und Freundlichkeit ausstrahlen.
Aufgabenstellung
Es soll ein Wiedererkennungswert zu unserer Homepage sein. In den Flyer sollen folgende Kriterien:
-> Vorne: Schönes Bild von unserer HP, unser Slogan: Für Menschen. Aus Leidenschaft. und unser Logo
Weitere Inhalte/Seiten:
-> Kontakt mit Bild der jew. Ansprechpartner: Ich freue mich auf Ihre Kontaktaufnahme!
-> über uns mit folgendem Text:
'Wenn ein Mensch im Familien- oder Bekanntenkreis pflegebedürftig wird, stehen Angehörige meist vor einer großen Herausforderung und vielen Fragen. Wir sind Ihr Ansprechpartner und haben das Anliegen, pflegebedürftigen Menschen mit einer osteuropäischen liebevollen Betreuungskraft den Verbleib im eigenen Zuhause zu ermöglichen. '
-> Aufgaben der Betreuungskraft
- Grundpflege
Hilfe bei der Körperpflege, An- und auskleiden, Toilettengänge, Unterstützung beim Aufstehen usw.
- Haushaltshilfe
Aufräumen, Staubsaugen, Wäsche waschen, Geschirr spülen und mehr
- Kochen und Ernährung
sorgt sich um das leibliche Wohl inkl. Einhaltung Ernährungspläne, einkaufen von Lebensmitteln
- soziale Betreuung
Schutz vor Vereinsamung, spazieren gehen, Ausflüge, Pflege von Hobbies, Begleitung bei Arztbesuchen
Gerne mit schönen Symbolen
-> Warum belanoxa? siehe Homepage anlehnend an: Sechs Gründe, die für uns sprechen
-> Vier Schritte zu Ihrer Betreuungskraft siehe Homepage
Schrift Trenda
www.belanoxa,de

```html
<!DOCTYPE html>
<html lang="de">
<head>
<meta charset="utf-8">
<title>belanoxa – Flyer 24-Stunden-Pflege</title>
<link href="https://fonts.googleapis.com/css2?family=Playfair+Display:wght@900&family=Mulish:wght@400;600;700&display=swap" rel="stylesheet">
<style>
:root{
  --red:#d3313a;
  --pink:#fbeced;
  --white:#ffffff;
  --ink:#1d1d1d;
  --canvas:#d5d5d5;
  --photo-warm:#d9b9a4;
  --photo-soft:#ecd9cc;
}
*{margin:0;padding:0;box-sizing:border-box}
html,body{width:892px;height:1200px;overflow:hidden;background:var(--canvas)}
body{position:relative;font-family:"Mulish",sans-serif;color:var(--ink)}
.sheet{position:absolute;left:31px;width:831px;background:var(--white);overflow:hidden}
.sheet--outside{top:18px;height:557px}
.sheet--inside{top:600px;height:558px}
.panel{position:absolute;top:0;height:100%}
.serif{font-family:"Playfair Display",serif;font-weight:900;color:var(--red);line-height:1.1}
.pink{background:var(--pink)}
.abs{position:absolute}
.photo{position:absolute;background:linear-gradient(135deg,var(--photo-soft),var(--photo-warm))}
.body-text{font-size:10.5px;line-height:13.6px}
.strip{position:absolute;left:0;bottom:0;width:100%;height:19px;background:var(--pink)}

/* outside */
.about{left:0;width:274px}
.about__head{left:0;top:0;width:274px;height:260px}
.about__title{left:41px;top:22px;font-size:20px}
.about__text{left:41px;top:79px;width:200px}
.about__text p+p{margin-top:13.6px}
.about__photo{left:0;top:260px;width:274px;height:205px}
.about__claim{left:42px;top:480px;font-size:21px}

.contact{left:274px;width:279px}
.contact__title{left:31px;top:24px;font-size:19.5px}
.contact__sub{left:31px;top:114px;font-size:15px;font-weight:700;color:var(--red)}
.portrait{position:absolute;left:21px;width:106px;height:106px;border-radius:50%;border:2px solid var(--red);background:radial-gradient(circle at 50% 40%,#f1ddd0,#e6e4e0)}
.person{position:absolute;left:136px;font-size:10px;line-height:12.7px}
.person__name{font-weight:700;font-size:11px;margin-bottom:12px}
.person__area{margin-bottom:12px}
.company{left:78px;top:468px;font-size:11px;line-height:14.2px}
.company li{list-style:none;display:flex;align-items:center;gap:5px}
.company svg{width:9px;height:9px;fill:var(--red)}

.front{left:553px;width:278px}
.front__head{left:0;top:0;width:278px;height:96px}
.front__title{left:38px;top:26px;font-size:23.5px}
.front__photo{left:0;top:96px;width:278px;height:340px}
.brand{left:2px;top:442px;display:flex;align-items:center;gap:10px}
.brand__dot{width:72px;height:72px;border-radius:50%;border:3px solid var(--red)}
.brand__name{font-size:40px;font-weight:400;color:var(--red);letter-spacing:1px}

/* inside */
.col-head{position:absolute;top:0;height:68px;width:100%}
.col-title{position:absolute;font-size:19.5px}
.tasks{left:0;width:279px}
.reasons{left:279px;width:279px}
.steps{left:558px;width:273px}
.item{position:absolute;left:61px;width:200px}
.item__title{font-size:11px;font-weight:700;margin-bottom:4px}
.item__icon{position:absolute;left:-46px;top:14px;width:36px;height:36px;fill:var(--red);stroke:var(--red)}
.reason{position:absolute;left:26px;width:238px}
.reason__title{font-size:11px;font-weight:700;color:var(--red);margin-bottom:5px}
.steps .item{left:66px;width:192px}
.steps .item__icon{left:-52px;top:10px}
.tasks__photo{left:0;top:387px;width:279px;height:171px}
.steps__photo{left:0;top:387px;width:273px;height:171px}
</style>
</head>
<body>

<section class="sheet sheet--outside">
  <div class="panel about">
    <div class="abs about__head pink"></div>
    <h2 class="abs serif about__title">Über uns</h2>
    <div class="abs about__text body-text">
      <p>Wenn ein Mensch im Familien- oder Bekanntenkreis pflegebedürftig wird, stehen Angehörige meist vor einer großen Herausforderung und vielen Fragen.</p>
      <p>Wir sind Ihr Ansprechpartner und haben das Anliegen, pflege­bedürftigen Menschen mit einer osteuropäischen liebevollen Betreuungskraft den Verbleib im eigenen Zuhause zu ermöglichen.</p>
    </div>
    <div class="photo about__photo" role="img" aria-label="Foto: ältere Dame und Betreuerin lehnen lächelnd die Köpfe aneinander"></div>
    <svg class="abs" style="left:0;top:360px" width="274" height="120" viewBox="0 0 274 120">
      <path d="M0 20 C40 90 150 115 274 90 L274 120 L0 120Z" fill="var(--white)"/>
      <path d="M0 40 C40 95 150 112 274 96 L274 104 C150 120 40 110 0 60Z" fill="var(--pink)"/>
      <path d="M0 20 C40 90 150 100 274 88 L274 94 C150 108 40 102 0 38Z" fill="var(--red)"/>
    </svg>
    <h2 class="abs serif about__claim">Wir sind für Sie da</h2>
  </div>

  <div class="panel contact">
    <h2 class="abs serif contact__title">Wir freuen uns auf Ihre<br>Kontaktaufnahme</h2>
    <h3 class="abs contact__sub">Ihre Ansprechpartner:</h3>
    <div class="portrait" style="top:164px" role="img" aria-label="Porträt der Ansprechpartnerin Maren Holt"></div>
    <div class="person" style="top:172px">
      <p class="person__name">Maren Holt</p>
      <p class="person__area">Landkreis Wiesental</p>
      <p>Tel.: 07100 412 3390<br>Mobil: 0176 000 318 52<br>Mail: m.holt@belanoxa.de</p>
    </div>
    <div class="portrait" style="top:301px" role="img" aria-label="Porträt der Ansprechpartnerin Ilse Brandt"></div>
    <div class="person" style="top:308px">
      <p class="person__name">Ilse Brandt</p>
      <p class="person__area">Landkreis Hohenmark<br>sowie bundesweite Anfragen</p>
      <p>Tel.: 07100 846 2217<br>Mobil: 0151 000 927 14<br>Mail: i.brandt@belanoxa.de</p>
    </div>
    <ul class="abs company">
      <li><svg viewBox="0 0 10 10"><path d="M5 0a3.5 3.5 0 0 0-3.5 3.5C1.5 6 5 10 5 10s3.5-4 3.5-6.5A3.5 3.5 0 0 0 5 0zm0 5a1.4 1.4 0 1 1 0-2.8A1.4 1.4 0 0 1 5 5z"/></svg>Lindenweg 14 | 70999 Falkenau</li>
      <li><svg viewBox="0 0 10 10"><path d="M2 0l2 2.5-1 1.2c.6 1.3 1.6 2.3 2.9 2.9l1.2-1L10 7.5 8.6 9.6C4 9.4.6 6 .4 1.4z"/></svg>Tel. 07100 / 84 21 530</li>
      <li><svg viewBox="0 0 10 10"><path d="M0 2h10v1L5 6 0 3zM0 4l5 3 5-3v4H0z"/></svg>info@belanoxa.de</li>
      <li><svg viewBox="0 0 10 10" fill="none" stroke="var(--red)" stroke-width="1"><circle cx="5" cy="5" r="4.3"/><ellipse cx="5" cy="5" rx="1.8" ry="4.3"/><path d="M.7 5h8.6M1.5 2.8h7M1.5 7.2h7"/></svg>https://www.belanoxa.de</li>
    </ul>
  </div>

  <div class="panel front">
    <div class="abs front__head pink"></div>
    <h1 class="abs serif front__title">Für Menschen.<br>Aus Leidenschaft.
      <svg width="22" height="20" viewBox="0 0 24 22" style="vertical-align:-1px;margin-left:4px"><path d="M12 20S2 13.5 2 7.2A5 5 0 0 1 12 5a5 5 0 0 1 10 2.2C22 13.5 12 20 12 20z" fill="none" stroke="var(--red)" stroke-width="2"/></svg>
    </h1>
    <div class="photo front__photo" role="img" aria-label="Foto: lächelnde Betreuerin und ältere Dame Wange an Wange"></div>
    <svg class="abs" style="left:0;top:300px" width="278" height="140" viewBox="0 0 278 140">
      <path d="M0 128 C110 130 230 100 278 20 L278 140 L0 140Z" fill="var(--white)"/>
      <path d="M0 128 C110 132 230 105 278 28 L278 42 C230 115 110 140 0 136Z" fill="var(--pink)"/>
      <path d="M0 126 C110 128 230 98 278 14 L278 26 C230 108 110 134 0 130Z" fill="var(--red)"/>
    </svg>
    <div class="abs brand">
      <span class="brand__dot"></span>
      <span class="brand__name">belanoxa</span>
    </div>
  </div>
  <div class="strip"></div>
</section>

<section class="sheet sheet--inside">
  <div class="panel tasks">
    <div class="col-head pink"></div>
    <h2 class="col-title serif" style="left:61px;top:14px">Aufgaben der<br>Betreuungskraft</h2>
    <div class="item" style="top:78px">
      <svg class="item__icon" viewBox="0 0 36 36"><rect x="2" y="18" width="32" height="3" rx="1"/><path d="M5 21h26l-3 8H8z"/><path d="M28 18V8a3 3 0 0 1 6 0" fill="none" stroke-width="2"/><circle cx="20" cy="10" r="1.5"/><circle cx="23" cy="7" r="1.5"/></svg>
      <p class="item__title">Grundpflege</p>
      <p class="body-text" style="font-size:10px;line-height:12.8px">Hilfe bei der Körperpflege, An- und aus­kleiden, Toilettengänge, Unterstützung beim Aufstehen usw.</p>
    </div>
    <div class="item" style="top:160px">
      <svg class="item__icon" viewBox="0 0 36 36"><rect x="12" y="14" width="12" height="20" rx="2"/><rect x="8" y="4" width="16" height="7"/><rect x="3" y="5" width="5" height="4"/><circle cx="29" cy="5" r="1"/><circle cx="32" cy="8" r="1"/><circle cx="29" cy="10" r="1"/></svg>
      <p class="item__title">Haushaltshilfe</p>
      <p class="body-text" style="font-size:10px;line-height:12.8px">Aufräumen, Staubsaugen, Wäsche waschen, Geschirr spülen und mehr</p>
    </div>
    <div class="item" style="top:228px">
      <svg class="item__icon" viewBox="0 0 36 36"><path d="M5 14h26v12a6 6 0 0 1-6 6H11a6 6 0 0 1-6-6z"/><rect x="3" y="11" width="30" height="3" rx="1"/><rect x="15" y="7" width="6" height="3" rx="1"/><path d="M1 17h4M31 17h4" stroke-width="2"/></svg>
      <p class="item__title">Kochen und Ernährung</p>
      <p class="body-text" style="font-size:10px;line-height:12.8px">sorgt sich um das leibliche Wohl inkl. Ein­haltung Ernährungspläne, einkaufen von Lebensmitteln</p>
    </div>
    <div class="item" style="top:310px">
      <svg class="item__icon" viewBox="0 0 36 36"><path d="M20 16s-8-5-8-10a4 4 0 0 1 8-1 4 4 0 0 1 8 1c0 5-8 10-8 10z"/><path d="M2 24l6-4c3-2 6-1 9 0h7a2 2 0 0 1 0 4h-8 10l8-5a2 2 0 0 1 2 3l-10 8H10l-4 2z"/></svg>
      <p class="item__title">soziale Betreuung</p>
      <p class="body-text" style="font-size:10px;line-height:12.8px">Schutz vor Vereinsamung, spazieren gehen, Ausflüge, Pflege von Hobbies, Begleitung bei Arztbesuchen</p>
    </div>
    <div class="photo tasks__photo" role="img" aria-label="Foto: älterer Herr und Betreuerin schneiden gemeinsam Gemüse in der Küche"></div>
  </div>

  <div class="panel reasons pink">
    <h2 class="col-title serif" style="left:26px;top:14px">Sechs Gründe, die<br>für uns sprechen</h2>
    <div class="reason" style="top:82px"><p class="reason__title">Hoher Qualitätsstandard und Partnerauswahl</p><p class="body-text" style="font-size:10px;line-height:12.8px">Wir haben hohe Ansprüche an uns selbst – und diese haben wir auch an unsere Partner in Ost­europa. Wir arbeiten nur mit seriösen und trans­parenten Anbietern zusammen.</p></div>
    <div class="reason" style="top:164px"><p class="reason__title">Geprüfte Personalvorschläge</p><p class="body-text" style="font-size:10px;line-height:12.8px">Sie erhalten nur Personalvorschläge von Betreu­ungskräften, die zu Ihnen und Ihrer<br>Situation passen.</p></div>
    <div class="reason" style="top:246px"><p class="reason__title">Individuelle Beratung</p><p class="body-text" style="font-size:10px;line-height:12.8px">Wir erarbeiten eine auf Ihre Situation angepasste Lösung, die sowohl für den Pflegebedürftigen als auch für die Angehörigen stimmig ist.</p></div>
    <div class="reason" style="top:327px"><p class="reason__title">Transparenz</p><p class="body-text" style="font-size:10px;line-height:12.8px">Transparenz ist in diesem sensiblen Tätigkeitsfeld unerlässlich. Wir beraten Sie ehrlich, loyal und auf höchstem Standard.</p></div>
    <div class="reason" style="top:409px"><p class="reason__title">Realistische Preisgestaltung</p><p class="body-text" style="font-size:10px;line-height:12.8px">Wir garantieren, dass Sie bei uns immer hohe Leistungen zu fairen Preisen bekommen.</p></div>
    <div class="reason" style="top:490px"><p class="reason__title">Begleitete Anreise</p><p class="body-text" style="font-size:10px;line-height:12.8px">Damit sich alle Parteien wohlfühlen, bieten wir op­tional ein Kennenlernen sowie eine Einführung vor Ort an, damit sich jeder von Anfang an wohl fühlt.</p></div>
  </div>

  <div class="panel steps">
    <div class="col-head pink"></div>
    <h2 class="col-title serif" style="left:62px;top:13px">In vier Schritten zu<br>Ihrer Pflegekraft</h2>
    <div class="item" style="top:82px">
      <svg class="item__icon" viewBox="0 0 36 36"><path d="M8 4l6 7-3 3c2 4 5 7 9 9l3-3 7 6-4 5C14 31 5 22 4 8z"/><path d="M21 9a7 7 0 0 1 6 6M22 3a13 13 0 0 1 11 11" fill="none" stroke-width="2.5"/></svg>
      <p class="item__title">1. Ihre Anfrage</p>
      <p class="body-text" style="font-size:10px;line-height:12.8px">Sie beschreiben uns die Situation und schildern uns Ihre Wünsche an die osteuropäische Pflegekraft.</p>
    </div>
    <div class="item" style="top:164px">
      <svg class="item__icon" viewBox="0 0 36 36"><path d="M4 3h20v12l-8 9-2 7H4z"/><path d="M8 9h12M8 14h12M8 19h6" stroke="var(--white)" stroke-width="2"/><path d="M30 12l4 4-14 14-5 1 1-5z"/></svg>
      <p class="item__title">2. Angebot</p>
      <p class="body-text" style="font-size:10px;line-height:12.8px">Wir prüfen gemeinsam Ihren Bedarf und erstellen Ihnen anschließend ein persön­liches Angebot.</p>
    </div>
    <div class="item" style="top:246px">
      <svg class="item__icon" viewBox="0 0 36 36"><rect x="2" y="15" width="7" height="18" rx="1"/><path d="M11 16l6-7 2-7c3 0 4 3 3 7l-1 4h10a3 3 0 0 1 0 6 3 3 0 0 1-1 5 3 3 0 0 1-2 5H13l-2-2z"/></svg>
      <p class="item__title">3. Personalvorschläge</p>
      <p class="body-text" style="font-size:10px;line-height:12.8px">Sie wählen die für Sie passende Betreu­ungskraft aus und entscheiden sich für eine Zusammenarbeit mit uns.</p>
    </div>
    <div class="item" style="top:327px">
      <svg class="item__icon" viewBox="0 0 36 36"><path d="M18 4L2 18h5v14h8v-9h6v9h8V18h5z"/></svg>
      <p class="item__title">4. Ihre Pflegekraft</p>
      <p class="body-text" style="font-size:10px;line-height:12.8px">Die 24-Stunden-Pflege beginnt die Betreuung zum gewünschten Zeitpunkt.</p>
    </div>
    <div class="photo steps__photo" role="img" aria-label="Foto: Betreuerin und ältere Dame lesen gemeinsam am Tisch"></div>
  </div>
</section>

</body>
</html>
```